Our Kitchen Pantry is an online food market place that connects foodies who make or grow great food with

We would like a 1/2 A4 page size flyer in landscape to promote our new business. We would like to encourage new home foodies to sign up for a membership on our website www.ourkitchenpantrynz.co.nz and we would like customers who are looking for great food in their local community to search our website for their closest home foodie and support a neighbour who is growing or producing creative food locally

Target Market(s)

Creative food lovers

Industry/Entity Type

Landscape

Colors
acd037
f78f20
33b8a4

Requirements
Must have
• Food images and look groovy
• Must be easy to read and stand out on a notice board
• Website address www.ourkitchenpantrynz.co.nz
Nice to have
• We wish to use this flyer in multiple locations and wish to put in different contact details prior to printing

```html
<!DOCTYPE html>
<html lang="en">
<head>
<meta charset="utf-8">
<title>Our Kitchen Pantry – Flyer</title>
<link rel="stylesheet" href="https://fonts.googleapis.com/css2?family=Roboto+Condensed:wght@300;700&family=Arimo:wght@400;700&family=Nunito:wght@900&display=swap">
<style>
  :root {
    --stage: #6b6766;
    --paper: #ffffff;
    --ink-grey: #4a4a4a;
    --ink-dark: #222222;
    --orange: #f78f20;
    --orange-soft: #f6a253;
    --teal: #33b8a4;
    --teal-dark: #1fa596;
    --lime: #acd037;
  }
  * { box-sizing: border-box; margin: 0; padding: 0; }
  html, body { width: 1200px; height: 875px; overflow: hidden; }
  body { background: var(--stage); position: relative; }

  .flyer {
    position: absolute; left: 77px; top: 68px;
    width: 1045px; height: 737px;
    background: var(--paper); overflow: hidden;
  }

  .photo-cook {
    position: absolute; left: 0; top: 0; width: 400px; height: 737px;
    background:
      radial-gradient(ellipse 60% 40% at 45% 35%, #d9b8a4 0%, rgba(217,184,164,0) 70%),
      radial-gradient(ellipse 70% 25% at 40% 92%, #6ea843 0%, rgba(110,168,67,0) 70%),
      linear-gradient(180deg, #f1f1f0 0%, #e6e2de 55%, #d8d2cc 100%);
  }
  .photo-dish {
    position: absolute; left: 388px; top: 415px; width: 657px; height: 262px;
    background:
      radial-gradient(ellipse 40% 45% at 35% 40%, #b8742f 0%, rgba(184,116,47,0) 75%),
      radial-gradient(ellipse 40% 45% at 75% 35%, #c47c37 0%, rgba(196,124,55,0) 75%),
      linear-gradient(180deg, #8a5a2b 0%, #6f9a3a 60%, #c9d9a6 100%);
  }

  .headline {
    position: absolute; left: 407px; top: 26px;
    font-family: "Roboto Condensed", sans-serif; color: var(--ink-grey);
    white-space: nowrap;
    transform: scaleX(0.88); transform-origin: left top;
  }
  .headline__intro, .headline__tail { font-weight: 300; font-size: 42px; line-height: 48px; letter-spacing: -0.5px; }
  .headline__tail { letter-spacing: 0; }
  .headline__main { font-weight: 700; font-size: 60px; line-height: 62px; color: var(--orange-soft); letter-spacing: -0.5px; }

  .audience { position: absolute; left: 414px; width: 620px; display: flex; align-items: center; }
  .audience--seller { top: 203px; }
  .audience--buyer { top: 306px; }
  .audience__icon {
    width: 88px; height: 88px; flex: none; border-radius: 50%;
    background: var(--teal); border: 4px solid #fff;
    box-shadow: 0 1px 4px rgba(0,0,0,0.25);
    display: flex; align-items: center; justify-content: center;
  }
  .audience__text {
    margin-left: 22px; font-family: "Arimo", sans-serif; font-size: 18.5px;
    line-height: 24.5px; color: var(--ink-dark);
  }
  .audience__text strong { font-weight: 700; }

  .info-pill {
    position: absolute; left: 391px; top: 634px; width: 382px; height: 38px;
    border-radius: 19px; background: var(--orange); border: 3px solid #fff;
    font-family: "Arimo", sans-serif; font-weight: 700; font-size: 19px;
    color: #fff; display: flex; align-items: center; justify-content: center;
    letter-spacing: 0.2px;
  }
  .web-address {
    position: absolute; left: 338px; top: 680px;
    font-family: "Nunito", sans-serif; font-weight: 900; font-size: 30px;
    color: var(--teal-dark); letter-spacing: 0.3px;
    text-shadow: 0 0 3px #fff, 0 0 3px #fff;
    white-space: nowrap;
  }

  .brand {
    position: absolute; left: 828px; top: 560px; width: 190px;
    display: flex; align-items: center; gap: 10px;
  }
  .brand__dot { width: 34px; height: 34px; flex: none; border-radius: 50%; background: var(--lime); }
  .brand__name {
    font-family: "Roboto Condensed", sans-serif; font-weight: 700;
    font-size: 30px; line-height: 30px; color: #ffffff; text-transform: uppercase;
  }
</style>
</head>
<body>
  <main class="flyer">
    <div class="photo-cook" role="img" aria-label="Smiling home cook in a striped apron tossing a fresh green salad in a glass bowl in a bright kitchen"></div>
    <div class="photo-dish" role="img" aria-label="Close-up of grilled chicken slices on a salad with croutons, tomatoes and herbs"></div>

    <header class="headline">
      <p class="headline__intro">Be part of our exciting new</p>
      <h1 class="headline__main">Online Food Marketplace</h1>
      <p class="headline__tail">connecting foodies in your local community</p>
    </header>

    <section class="audience audience--seller">
      <div class="audience__icon">
        <svg width="44" height="44" viewBox="0 0 44 44" aria-hidden="true">
          <path d="M12 20a7 7 0 0 1 4-12 8 8 0 0 1 12 0 7 7 0 0 1 4 12v6H12z" fill="#fff"/>
          <rect x="12" y="29" width="20" height="5" fill="#fff"/>
          <rect x="6" y="37" width="32" height="3" fill="#fff"/>
        </svg>
      </div>
      <p class="audience__text"><strong>As a foodie</strong> you can sell your beautiful home<br>produced or home grown produce on our<br>marketplace website</p>
    </section>

    <section class="audience audience--buyer">
      <div class="audience__icon">
        <svg width="44" height="44" viewBox="0 0 44 44" aria-hidden="true">
          <path d="M13 6v12M9 6v8a4 4 0 0 0 8 0V6M13 18v20" stroke="#fff" stroke-width="3" fill="none" stroke-linecap="round"/>
          <path d="M30 38V6c-5 3-6 10-6 16h6" stroke="#fff" stroke-width="3" fill="none" stroke-linecap="round" stroke-linejoin="round"/>
        </svg>
      </div>
      <p class="audience__text"><strong>As a food lover</strong> you can purchase lovingly grown<br>or prepared food and support your local foodie<br>community while keeping your food miles low</p>
    </section>

    <div class="brand">
      <span class="brand__dot"></span>
      <span class="brand__name">Our Kitchen Pantry</span>
    </div>

    <p class="info-pill">FOR MORE INFORMATION GO TO</p>
    <p class="web-address">www.ourkitchenpantrynz.co.nz</p>
  </main>
</body>
</html>
```